Nimbo37.com.au Website and company image design

We are looking for an exceptional website designer / company to work with our new Australian Hosting Company

Nimbo37 is a new Cloud Hosting company launching in Australia that provides Scalable, On Demand computing resources to the Australian Market Place. Scalable, On Demand ocmputing is a nice way of saying fully scalable / redundant Virtual Private Server.

We require a full company image to be developed along with a Logo and Website. There is scope for ongoing development (preferred) for the successful candidate.

Website developement will require extensive jQuery ability (sliders for ordering etc (see: http://www.hostara.com.au/virtual-dedicated-servers/253/xen_vps.html).

Please communicate directly with me to establish full website scope and request further documentation / content.

Target Market(s)

Website Designers, programmers, technicians and large companies

Industry/Entity Type

It Company

Requirements
Must have
• Slider ordering system such as http://www.hostara.com.au/virtual-dedicated-servers/253/xen_vps.html

Nice to have
• CMS backend system
Should not have
• Should NOT be a monster template copy!!!

```html
<!DOCTYPE html>
<html lang="en">
<head>
<meta charset="utf-8">
<title>Nimbo37 – Cloud Hosting</title>
<link href="https://fonts.googleapis.com/css2?family=Noto+Sans:wght@400;700&family=Arimo:wght@400;700&display=swap" rel="stylesheet">
<style>
:root{
  --blue:#1e7ec8;
  --blue-dark:#1560a8;
  --blue-bg-top:#3b8fd4;
  --blue-bg-bot:#5aa5e0;
  --ink:#222;
  --grey:#777;
  --nav:#333;
  --rule:#d8d8d8;
  --panel:#e8f1fa;
  --green:#6cb043;
}
*{box-sizing:border-box;margin:0;padding:0}
html,body{width:720px;height:1200px;overflow:hidden}
body{position:relative;background:linear-gradient(var(--blue-bg-top),var(--blue-bg-bot));font-family:"Arimo",Arial,sans-serif;color:var(--ink)}
.abs{position:absolute}
.head-font{font-family:"Noto Sans",Arial,sans-serif}
.header{position:absolute;left:0;top:0;width:720px;height:340px;background:#fff}
.header-band{position:absolute;left:0;top:340px;width:720px;height:7px;background:#2e2e2e}
.logo{left:82px;top:16px;display:flex;align-items:center;gap:6px}
.logo-mark{width:22px;height:22px;border-radius:50%;background:var(--blue)}
.logo-name{font-family:"Noto Sans",sans-serif;font-weight:700;font-size:18px;color:#333}
.call{left:380px;top:39px;width:107px;text-align:right;font-family:"Noto Sans",sans-serif;font-weight:700;font-size:10.5px}
.phone{left:360px;top:50px;width:128px;text-align:right;font-family:"Noto Sans",sans-serif;font-weight:700;font-size:19px;color:var(--blue)}
.follow{display:flex;align-items:center;gap:3px;font-size:7px;color:#222}
.follow i{display:block;width:10px;height:10px;background:#9fb3c8;border-radius:2px}
.search{left:504px;top:54px;width:136px;height:15px;border-radius:3px;background:#222;color:#ddd;font-size:7.5px;padding:2px 8px}
.nav{left:72px;top:83px;width:577px;height:31px;background:var(--nav);display:flex;align-items:center;box-shadow:0 6px 6px -3px rgba(0,0,0,.45)}
.nav a{color:#fff;font-family:"Noto Sans",sans-serif;font-weight:700;font-size:8px;text-decoration:none;flex:1;text-align:center;border-left:1px solid #555;line-height:18px}
.nav a:first-child{flex:0 0 auto;margin:0 10px;background:#fff;color:#222;border:none;border-radius:2px;padding:0 7px;line-height:14px}
.nav a:nth-child(2){border-left:none}
.arrow{width:25px;height:24px;background:#ccc;border-radius:2px}
.hero-title{left:131px;top:157px;font-family:"Noto Sans",sans-serif;font-weight:700;font-size:20px;color:#333}
.hero-sub{left:131px;top:183px;font-family:"Noto Sans",sans-serif;font-size:16px;color:#333}
.hero-sub b{color:var(--blue)}
.hero-copy{left:132px;top:213px;width:190px;font-size:7.5px;line-height:12px;color:#999}
.btn-quote{left:130px;top:270px;width:133px;height:27px;border:2px solid #aac;background:var(--blue-dark);color:#fff;font-family:"Noto Sans",sans-serif;font-weight:700;font-size:10.5px;display:flex;align-items:center;justify-content:center}
.hero-art{left:355px;top:142px;width:236px;height:178px;border-radius:50%;background:radial-gradient(#bfe0f6,#fff 72%)}
.main{left:72px;top:346px;width:577px;height:826px;background:#fff}
.globe{left:99px;top:366px;width:144px;height:94px;background:linear-gradient(135deg,#0d4f9a,#4eb0ea 60%,#a7dcf7)}
.intro-h{left:256px;top:366px;font-family:"Noto Sans",sans-serif;font-weight:700;font-size:14.5px;color:#222}
.intro-p{left:257px;top:392px;width:365px;font-size:7px;line-height:15px;color:#222}
.more{left:567px;top:456px;font-size:6.5px;font-weight:700;color:var(--blue);display:flex;gap:4px;align-items:center}
.more i{display:block;width:7px;height:7px;border-radius:50%;background:#555}
.rule{height:1px;background:var(--rule)}
.feat-h{font-family:"Noto Sans",sans-serif;font-weight:700;font-size:11px}
.feat-p{font-size:8px;line-height:10.5px;color:#333;margin-top:2px}
.side-box{left:99px;top:580px;width:123px;height:89px;background:#f3f3f3;border:1px solid #ddd}
.side-box h3{background:var(--blue);color:#fff;font-family:"Noto Sans",sans-serif;font-size:8.5px;padding:5px 7px;height:20px}
.side-box li{list-style:none;font-size:7.5px;color:#333;margin:0 16px 0 7px;padding:3px 0 3px;border-bottom:1px solid #ccc;line-height:9.5px}
.side-box li:last-child{border:none}
.domain{left:99px;top:687px;width:123px;height:90px;background:linear-gradient(var(--blue),#1d6eb5);color:#fff;text-align:center}
.domain h3{font-family:"Noto Sans",sans-serif;font-size:11.5px;line-height:11px;margin-top:10px}
.domain .inp{position:absolute;left:9px;top:44px;width:45px;height:13px;background:#fff;border-radius:2px}
.domain .tld{position:absolute;left:61px;top:44px;width:51px;height:13px;background:#ddd;border-radius:2px;color:#333;font-size:7.5px;line-height:13px}
.domain .chk{position:absolute;left:25px;top:66px;width:69px;height:15px;background:#444;border-radius:3px;font-size:8px;line-height:15px}
.side-art{left:101px;top:795px;width:120px;height:84px;border:1px solid #ccc;background:linear-gradient(#f5f7fa,#d9e8d4)}
.build-h{left:252px;top:574px;font-family:"Noto Sans",sans-serif;font-weight:700;font-size:23px;color:var(--blue)}
.panel{left:251px;top:617px;width:365px;height:276px;background:var(--panel);border:1px solid #d3e2f0;border-radius:3px}
.lbl{font-family:"Noto Sans",sans-serif;font-weight:700;font-size:8.5px;color:var(--blue-dark)}
.select{left:267px;top:649px;width:207px;height:16px;background:#fff;border:1px solid #bbb;border-radius:2px;font-size:7.5px;padding:3px 7px;color:#444}
.row-l{left:268px;font-size:8.5px;color:#222}
.row-l b{font-family:"Noto Sans",sans-serif}
.row-v{left:540px;width:51px;text-align:right;font-family:"Noto Sans",sans-serif;font-weight:700;font-size:8.5px;color:var(--blue)}
.track{left:268px;width:323px;height:4px;border-radius:2px;background:linear-gradient(90deg,var(--green) 0 48%,#999 48%)}
.knob{position:absolute;left:151px;top:-4px;width:10px;height:10px;border-radius:50%;background:#fff;border:1px solid #aaa}
.price{left:399px;top:907px;width:137px;height:20px;background:#eee;border:1px solid #bbb;font-family:"Noto Sans",sans-serif;font-weight:700;font-size:10.5px;line-height:18px;text-align:center}
.signup{left:536px;top:907px;width:80px;height:20px;background:var(--blue);color:#fff;font-family:"Noto Sans",sans-serif;font-weight:700;font-size:11px;line-height:20px;text-align:center}
.partner{top:962px;height:30px;background:#d4d4d4;border-radius:3px}
.foot-col h4{font-size:8px;font-weight:400;color:#222;margin-bottom:10px}
.foot-col li{list-style:none;font-size:7px;line-height:10.2px;color:#333}
.copy{left:103px;top:1150px;font-size:6.5px;color:#333}
</style>
</head>
<body>
<div class="header">
  <div class="abs logo"><span class="logo-mark"></span><span class="logo-name">Nimbo37</span></div>
  <div class="abs follow" style="left:548px;top:32px">Follow Us <i></i><i></i><i></i><i></i></div>
  <div class="abs call">Call Us 24x7x365</div>
  <div class="abs phone">800.555.0142</div>
  <div class="abs search">Search</div>
  <nav class="abs nav">
    <a>Home</a><a>Domains</a><a>Web Hosting</a><a>Virtual Servers</a><a>Dedicated Servers</a><a>Resellers</a><a>About Us</a>
  </nav>
  <div class="abs arrow" style="left:72px;top:218px"></div>
  <div class="abs arrow" style="left:624px;top:218px"></div>
  <h1 class="abs hero-title">Cloud Hosting Servers</h1>
  <p class="abs hero-sub">starting from <b>$49/month</b></p>
  <p class="abs hero-copy">Lorem ipsum dolor sit amet, consectetur adipiscing elit. In vulputate iaculis sapien et condimentum. In posuere, dui et vestibulum suscipit, mi felis egestas felis, ut.</p>
  <div class="abs btn-quote">REQUEST A QUOTE ›</div>
  <div class="abs hero-art" role="img" aria-label="Cloud at the centre linked by arrows to servers, desktops, laptops and phones"></div>
</div>
<div class="header-band"></div>

<div class="abs main"></div>
<div class="abs globe" role="img" aria-label="Blue glowing globe"></div>
<h2 class="abs intro-h">Our experience in Cloud Hosting projects.</h2>
<p class="abs intro-p">Lorem ipsum dolor sit amet, consectetur adipisicing elit, sed do eiusmod tempor incididunt ut labore et dolore magna aliqua. Ut enim ad minim veniam, quis nostrud exercitation ullamco laboris nisi ut aliquip ex commodo consequat. Duis aute irure dolor in reprehenderit in voluptate velit esse cillum dolore eu fugiat nulla pariatur. Excepteur sint occaecat cupidatat non proident, sunt in culpa qui officia deserunt mollit anim id est laborum.</p>
<div class="abs more"><i></i>Read More</div>

<div class="abs rule" style="left:102px;top:484px;width:512px"></div>
<svg class="abs" style="left:116px;top:502px" width="34" height="34" viewBox="0 0 34 34">
  <rect x="1" y="20" width="9" height="13" fill="#d9302a"/><rect x="12" y="2" width="9" height="31" fill="#5bb33c"/><rect x="23" y="12" width="9" height="21" fill="#f0b323"/>
</svg>
<div class="abs" style="left:169px;top:502px"><div class="feat-h">Performance</div><div class="feat-p">When speed matter<br>most</div></div>
<div class="abs" role="img" aria-label="Forklift carrying a green crate" style="left:300px;top:502px;width:36px;height:36px;background:linear-gradient(#9fc24a,#e6c33a);border-radius:4px"></div>
<div class="abs" style="left:357px;top:502px"><div class="feat-h">Scalability</div><div class="feat-p">Handle Your growth<br>in a graceful manner</div></div>
<div class="abs" role="img" aria-label="Red support manual" style="left:490px;top:502px;width:30px;height:30px;background:linear-gradient(#e43a32,#b11d18);border-radius:3px"></div>
<div class="abs" style="left:537px;top:502px"><div class="feat-h">Support</div><div class="feat-p">24/7 Dedicated<br>Specialists</div></div>
<div class="abs rule" style="left:102px;top:556px;width:512px"></div>

<div class="abs side-box">
  <h3>Cloud VPS</h3>
  <ul><li>Kestrel VPS</li><li>Vireo VPS</li><li>Orbis VPS</li><li>VDS Backup</li></ul>
</div>
<div class="abs domain">
  <h3>Domain Name<br>Search</h3>
  <div class="inp"></div><div class="tld">.com.au ▾</div><div class="chk">Check Domain</div>
</div>
<div class="abs side-art" role="img" aria-label="Private cloud server scalability diagram"></div>

<h2 class="abs build-h">BUILD YOUR SERVER</h2>
<div class="abs panel"></div>
<div class="abs lbl" style="left:268px;top:628px">Select Your Operating System</div>
<div class="abs select">Corvo OS 6<span style="float:right">▾</span></div>
<div class="abs lbl" style="left:268px;top:676px;text-decoration:underline">Customise your system</div>

<div class="abs row-l" style="top:696px"><b>CPU cores</b> ($15.00 per month)</div><div class="abs row-v" style="top:696px">4 cores</div>
<div class="abs track" style="top:717px"><span class="knob"></span></div>
<div class="abs row-l" style="top:733px"><b>Disk Space</b> ($0.49 per month)</div><div class="abs row-v" style="top:733px">440 GB</div>
<div class="abs track" style="top:753px"><span class="knob"></span></div>
<div class="abs row-l" style="top:770px"><b>Dedicated RAM</b> ($30.00 per month)</div><div class="abs row-v" style="top:770px">4 GB</div>
<div class="abs track" style="top:790px"><span class="knob"></span></div>
<div class="abs row-l" style="top:809px"><b>Premium Bandwidth</b> ($0.55 per month)</div><div class="abs row-v" style="top:809px">885 GB</div>
<div class="abs track" style="top:829px"><span class="knob"></span></div>
<div class="abs row-l" style="top:847px"><b>IP Addresses</b> ($3.50 per month)</div><div class="abs row-v" style="top:847px">13 IPs</div>
<div class="abs track" style="top:867px"><span class="knob"></span></div>

<div class="abs price">Monthly Price: $927.85</div>
<div class="abs signup">SIGN UP ›</div>

<div class="abs rule" style="left:102px;top:941px;width:512px"></div>
<div class="abs partner" style="left:105px;width:90px"></div>
<div class="abs partner" style="left:225px;width:68px"></div>
<div class="abs partner" style="left:322px;width:60px"></div>
<div class="abs partner" style="left:410px;width:52px"></div>
<div class="abs partner" style="left:496px;width:46px"></div>
<div class="abs partner" style="left:573px;width:40px"></div>

<div class="abs foot-col" style="left:103px;top:1027px"><h4>Web Hosting</h4><ul><li>Winvale or Linnex?</li><li>Linnex Hosting</li><li>Winvale Hosting</li><li>SSL Certificates</li><li>Advanced WebMail</li><li>Active Spam Filtering</li><li>Hosting Control Panel</li><li>Application Vaul</li></ul></div>
<div class="abs foot-col" style="left:245px;top:1027px"><h4>Virtual Servers</h4><ul><li>Linnex VPS</li><li>Winvale VPS</li><li>Winvale Tessel VPS</li><li>Linnex Tessel VPS</li><li>Tessel Hosting VPS</li><li>Helmpanel Virtual Servers</li><li>Quickstart Add-on</li><li>Helmpanel VPS</li></ul></div>
<div class="abs foot-col" style="left:385px;top:1027px"><h4>Dedicated Servers</h4><ul><li>Same-Day Dedicated</li><li>Small Business Servers</li><li>Medium Business Servers</li><li>Enterprise Servers</li><li>Winvale Dedicated</li><li>Servers</li><li>Backup and Recovery</li><li>Data Center</li></ul></div>
<div class="abs foot-col" style="left:533px;top:1027px"><h4>About Nimbo37</h4><ul><li>About Nimbo37</li><li>Partners</li><li>Terms of Service</li><li>Service Level Agreement</li><li>Privacy Policy</li><li>Refund Policy</li><li>Jobs @ Nimbo37</li><li>Contact Us</li></ul></div>

<div class="abs copy">© 2012, Brightframe , All Rights Reserved</div>
<div class="abs follow" style="left:527px;top:1147px">Follow Us <i></i><i></i><i></i><i></i></div>
</body>
</html>
```